NEW Brand "New Zealand Wine Estate"

We are looking for a design for our new range of New Zealand wine. An estate label that can be used for several varietals.
We have three potential names...
Hollow Pine Estate
Amber Lantern Estate
Morvina Estate
first variant is "Central Otago Pinot Noir" please use this in the original design.
This brand is for world export, so will need to be appealing to many markets but representative of New Zealand and our rugged Coasts.
Target Market(s)
Supermarket $25 NZD per bottle price point. Young and hip
Font styles to use
Decorative
Script
Requirements
Must have
- Sophistication but edgy. Stand out on a shelf.
- the brand needs to be able to be used for red or white wine.

```html
<!DOCTYPE html>
<html lang="en">
<head>
<meta charset="utf-8">
<title>Morvina Estate – Central Otago Pinot Noir Label</title>
<link rel="stylesheet" href="https://fonts.googleapis.com/css2?family=Kaushan+Script&family=Montserrat:wght@400;500;600&display=swap">
<style>
  :root {
    --backdrop: #e4e4e4;
    --label-paper: #f2f2f0;
    --label-rim: #8c8178;
    --ink-dark: #2b2b2d;
    --ink-soft: #5b5754;
    --accent-pink: #e2295f;
    --art-light: #e6e6e4;
    --art-dark: #9a9a98;
  }
  * { margin: 0; padding: 0; box-sizing: border-box; }
  html, body {
    width: 1200px;
    height: 2808px;
    overflow: hidden;
    background: var(--backdrop);
  }
  .canvas {
    position: relative;
    width: 1200px;
    height: 2808px;
  }
  .wine-label {
    position: absolute;
    left: 125px;
    top: 39px;
    width: 950px;
    height: 2730px;
    background: var(--label-paper);
    border: 7px solid var(--label-rim);
    border-radius: 475px / 430px;
    box-shadow: inset 0 0 0 14px var(--label-paper), inset 0 0 0 16px #cfc9c3;
    font-family: "Montserrat", sans-serif;
    color: var(--ink-dark);
    text-align: center;
  }
  .tagline-arc {
    position: absolute;
    left: 0;
    top: 0;
    width: 936px;
    height: 600px;
  }
  .tagline-arc text {
    font-family: "Montserrat", sans-serif;
    font-weight: 500;
    font-size: 33px;
    letter-spacing: 4px;
    fill: var(--ink-dark);
  }
  .ship-artwork {
    position: absolute;
    left: 185px;
    top: 360px;
    width: 566px;
    height: 880px;
    border-radius: 40px;
    background: radial-gradient(ellipse at 50% 45%, var(--art-light) 0%, #d2d2d0 55%, var(--art-dark) 100%);
    opacity: 0.75;
  }
  .brand-name {
    position: absolute;
    left: 0;
    right: 0;
    top: 1340px;
    font-family: "Kaushan Script", cursive;
    font-weight: 400;
    color: var(--ink-dark);
    line-height: 1;
  }
  .brand-name .brand-main { display: block; font-size: 245px; }
  .brand-name .brand-sub { display: block; font-size: 170px; margin-top: 10px; }
  .vintage {
    position: absolute;
    left: 0;
    right: 0;
    top: 2065px;
    display: flex;
    justify-content: center;
    align-items: center;
    gap: 22px;
    font-size: 56px;
    font-weight: 500;
    letter-spacing: 6px;
    color: var(--ink-dark);
  }
  .vintage .rule {
    width: 95px;
    height: 4px;
    background: var(--ink-soft);
  }
  .bottle-facts {
    position: absolute;
    left: 0;
    right: 0;
    top: 2300px;
    font-size: 54px;
    font-weight: 500;
    line-height: 1.25;
    letter-spacing: 2px;
  }
  .varietal {
    position: absolute;
    left: 0;
    right: 0;
    top: 2470px;
    line-height: 1.1;
  }
  .varietal .region {
    display: block;
    font-size: 44px;
    letter-spacing: 9px;
    color: var(--ink-soft);
    font-weight: 400;
  }
  .varietal .grape {
    display: block;
    font-size: 80px;
    letter-spacing: 4px;
    font-weight: 600;
    color: var(--accent-pink);
  }
</style>
</head>
<body>
<main class="canvas">
  <section class="wine-label">
    <svg class="tagline-arc" viewBox="0 0 936 600" aria-hidden="false">
      <defs>
        <path id="tagline-path" d="M 90 560 A 378 420 0 0 1 846 560" fill="none"/>
      </defs>
      <text><textPath href="#tagline-path" startOffset="50%" text-anchor="middle">CLASSIC, PASSIONATE &amp; UNIQUELY NEW ZEALAND WINE</textPath></text>
    </svg>

    <div class="ship-artwork" role="img" aria-label="Pencil-style illustration of a tall sailing ship with billowing sails on rough sea"></div>

    <h1 class="brand-name">
      <span class="brand-main">Morvina</span>
      <span class="brand-sub">Estate</span>
    </h1>

    <p class="vintage"><span class="rule"></span>2016<span class="rule"></span></p>

    <p class="bottle-facts">18%<br>75 CL.</p>

    <p class="varietal">
      <span class="region">CENTRAL OTAGO</span>
      <span class="grape">PINOT NOIR</span>
    </p>
  </section>
</main>
</body>
</html>
```